Quolvex custom business card design

Need a authentic, innovative business card design for a new mobile app business. I am uploading a few screen images from our app for you to view. I would like app design theme to match business card design. I can also send logo images.

```html
<!DOCTYPE html>
<html lang="en">
<head>
<meta charset="UTF-8">
<title>Quolvex Business Card</title>
<link href="https://fonts.googleapis.com/css2?family=Work+Sans:wght@400;500;800&display=swap" rel="stylesheet">
<style>
  :root {
    --page-bg: #e6ded3;
    --card-bg: #f6f3ef;
    --card-edge: #dcd5cc;
    --ink-dark: #262626;
    --ink-body: #4a4a4a;
    --accent-purple: #5b2474;
    --mark-fill: #3a2a40;
  }
  * { margin: 0; padding: 0; box-sizing: border-box; }
  html, body {
    width: 1200px;
    height: 1047px;
    overflow: hidden;
    background: var(--page-bg);
    font-family: "Work Sans", Arial, sans-serif;
  }
  .business-card {
    position: absolute;
    left: 80px;
    top: 233px;
    width: 1040px;
    height: 580px;
    background: var(--card-bg);
    border: 2px solid var(--card-edge);
    border-radius: 22px;
    box-shadow: 0 10px 30px rgba(60, 45, 30, 0.15);
  }
  .brand-name {
    position: absolute;
    left: 50px;
    top: 38px;
    font-weight: 800;
    font-size: 80px;
    letter-spacing: -1px;
    color: var(--ink-dark);
    line-height: 1;
  }
  .person-name {
    position: absolute;
    left: 52px;
    top: 190px;
    font-weight: 500;
    font-size: 37px;
    letter-spacing: 1px;
    color: var(--accent-purple);
  }
  .person-title {
    position: absolute;
    left: 52px;
    top: 238px;
    font-size: 24px;
    letter-spacing: 0.5px;
    color: var(--ink-body);
  }
  .address {
    position: absolute;
    left: 52px;
    top: 292px;
    font-size: 25px;
    line-height: 38px;
    letter-spacing: 0.8px;
    color: var(--ink-body);
  }
  .contact-list {
    position: absolute;
    left: 52px;
    top: 388px;
    list-style: none;
  }
  .contact-item {
    display: flex;
    align-items: center;
    height: 37px;
    font-size: 25px;
    letter-spacing: 0.8px;
    color: var(--ink-body);
  }
  .contact-icon {
    width: 22px;
    height: 22px;
    margin-right: 15px;
    flex-shrink: 0;
  }
  .brand-disc {
    position: absolute;
    left: 494px;
    top: 24px;
    width: 512px;
    height: 512px;
    border-radius: 50%;
    background: var(--mark-fill);
  }
</style>
</head>
<body>
  <main class="business-card">
    <div class="brand-name">Quolvex</div>
    <div class="person-name">DANIEL HARPER</div>
    <div class="person-title">Director</div>
    <address class="address" style="font-style: normal;">
      1427 Harbor Lane<br>
      Palm Coast, FL 32137
    </address>
    <ul class="contact-list">
      <li class="contact-item">
        <svg class="contact-icon" viewBox="0 0 24 24" fill="none" stroke="#5b2474" stroke-width="2.2"><rect x="6" y="2" width="12" height="20" rx="2"/><line x1="11" y1="18" x2="13" y2="18"/></svg>
        (555) 201-4837
      </li>
      <li class="contact-item">
        <svg class="contact-icon" viewBox="0 0 24 24" fill="none" stroke="#5b2474" stroke-width="2.2" stroke-linejoin="round"><path d="M5 3h4l2 5-2.5 1.5a11 11 0 0 0 6 6L16 13l5 2v4a2 2 0 0 1-2 2A17 17 0 0 1 3 5a2 2 0 0 1 2-2z"/></svg>
        (555) 201-4926
      </li>
      <li class="contact-item">
        <svg class="contact-icon" viewBox="0 0 24 24" fill="none" stroke="#5b2474" stroke-width="2.2"><rect x="2" y="5" width="20" height="14" rx="1.5"/><polyline points="2,6 12,13 22,6"/></svg>
        info@Quolvex.com
      </li>
      <li class="contact-item">
        <svg class="contact-icon" viewBox="0 0 24 24" fill="none" stroke="#5b2474" stroke-width="2"><circle cx="12" cy="12" r="10"/><ellipse cx="12" cy="12" rx="4.5" ry="10"/><line x1="2" y1="12" x2="22" y2="12"/></svg>
        www.Quolvex.com
      </li>
    </ul>
    <div class="brand-disc" role="img" aria-label="Brand mark area"></div>
  </main>
</body>
</html>
```